Billboard for Law Firm

I am looking for a billboard designs. Our branding right now is not good. The logo has to stay the same, but please help come up with something modern, airy, perhaps geometric for the supporting design elements.
Colors should probably be red and blue, or shades of blue, but you can play with the exact shades. Doesn't have to match what you see in the attachment.

The billboard should include:

- Some type of design to bring it to life.

- Logo

- Accident & Injury Law

- 614.355.7182

- Disclaimer (very small text): No Representation Made That The Quality of Legal Services Performed is Greater Than the Those of Other Attorneys

Slogan (very large): Grits, Gravy, and a Good Attorney

______________
Thank You For Your Participation!

Target Market(s)

Southern United States

Industry/Entity Type

Legal Services

Font styles to use
Serif
Sans Serif

Colors
0054AA
0677BA
7BADD7
CADEEF
E8F1F8
EB3D1F
EC4F4E
F09395
F8D3D4
FCEDEE

Requirements
Must have
• Help Make it Memorable and Easy to Read (large text for slogan)
Nice to have
• Some shapes or design elements that may become part of our branding.

```html
<!DOCTYPE html>
<html lang="en">
<head>
<meta charset="utf-8">
<title>Billboard – Accident &amp; Injury Law</title>
<link rel="stylesheet" href="https://fonts.googleapis.com/css2?family=Montserrat:wght@300;600;700;800&display=swap">
<style>
  :root {
    --navy: #1b2232;
    --band: #d22b27;
    --white: #ffffff;
  }
  html, body {
    margin: 0;
    padding: 0;
    width: 1200px;
    height: 613px;
    overflow: hidden;
    background: var(--navy);
  }
  .billboard {
    position: relative;
    width: 1200px;
    height: 613px;
    overflow: hidden;
    background: var(--navy);
    font-family: "Montserrat", sans-serif;
    color: var(--white);
  }
  .artwork {
    position: absolute;
    inset: 0;
    width: 1200px;
    height: 613px;
  }
  .brand {
    position: absolute;
    top: 56px;
    right: 54px;
    display: flex;
    align-items: center;
    gap: 8px;
    margin: 0;
    color: var(--band);
    font-weight: 700;
    font-size: 19px;
    line-height: 24px;
    white-space: nowrap;
  }
  .brand-dot {
    width: 13px;
    height: 13px;
    border-radius: 50%;
    background: var(--band);
  }
  .slogan {
    position: absolute;
    top: 137px;
    right: 42px;
    margin: 0;
    text-align: right;
    font-weight: 700;
    font-size: 46px;
    line-height: 58px;
    letter-spacing: 0;
    text-transform: uppercase;
    white-space: nowrap;
  }
  .rule {
    position: absolute;
    left: 771px;
    top: 296px;
    width: 379px;
    height: 5px;
    background: var(--band);
  }
  .practice,
  .phone {
    position: absolute;
    right: 45px;
    margin: 0;
    font-weight: 700;
    font-size: 21px;
    line-height: 26px;
    white-space: nowrap;
  }
  .practice { top: 348px; letter-spacing: -0.4px; }
  .phone { top: 387px; right: 48px; }
  .disclaimer {
    position: absolute;
    top: 502px;
    right: 46px;
    margin: 0;
    text-align: right;
    font-weight: 300;
    font-size: 14.5px;
    line-height: 22px;
    white-space: nowrap;
  }
</style>
</head>
<body>
<main class="billboard">
  <svg class="artwork" viewBox="0 0 2576 1316" preserveAspectRatio="none">
    <defs>
      <linearGradient id="photoTone" x1="0" y1="0" x2="1" y2="0.3">
        <stop offset="0" stop-color="#6d6c70"/>
        <stop offset="0.35" stop-color="#8e7a6c"/>
        <stop offset="0.7" stop-color="#2e3445"/>
        <stop offset="1" stop-color="#1f2535"/>
      </linearGradient>
    </defs>
    <path class="photo-area" role="img" aria-label="Photo of an attorney in a pinstripe suit adjusting his tie, wearing a wristwatch"
          fill="url(#photoTone)"
          d="M0 0 L940 0 L1160 1316 L0 1316 Z"/>
    <path class="accent-band" fill="var(--band)"
          d="M940 0 L1200 0 L1480 1316 L1160 1316 Z"/>
  </svg>

  <p class="brand"><span class="brand-dot"></span>The Hartwell Firm</p>

  <h1 class="slogan">Grits, Gravy, and<br>a Good Attorney</h1>

  <div class="rule"></div>

  <p class="practice">ACCIDENT &amp; INJURY LAW</p>
  <p class="phone">614.355.7182</p>

  <p class="disclaimer">No Representation Made That The Quality<br>of Legal Services Performed is Greater<br>Than the Those of Other Attorneys</p>
</main>
</body>
</html>
```